Business Card Design Project

Hello! We need a business card design for a new company opening up in Downtown Dallas called Marbrook Cupcakes. We are a cupcake factory and our primary colors are Harbor Teal and Brown. We want to have a design that can be used for multiple positions (Owner/Operations Manager, Assistant Operations Manager, Decorator, Baker, Corporate Sale Rep, Special Events Rep etc) We would like for it to be double sided. Use the following information in your designs:

Renata Vasquill
Assistant Operations Manager
renata@marbrookcupcakes.example
T555.318.9047

Store Hours:
Mon-Thur 10am-9pm
Fri-Sat 10am-10pm
Sun 12pm-7pm

website: www.marbrookcupcakes.example

Address: 2735 Quarry Ln, Dallas TX 75999

The logo is attached.

Industry/Entity Type

Business

Requirements
Must have
• It must be Harbor Teal and Brown.
Nice to have
• Nice for it to be double sided.
Should not have
• No graphics like a cupcake. Just the word logo.

```html
<!DOCTYPE html>
<html lang="en">
<head>
<meta charset="utf-8">
<title>Marbrook Cupcakes – Business Card</title>
<link rel="stylesheet" href="https://fonts.googleapis.com/css2?family=Questrial&display=swap">
<style>
  :root {
    --harbor-teal: #5ec4c5;
    --teal-deep: #4fb5b7;
    --cocoa: #3a2420;
    --paper: #ffffff;
    --backdrop: #ece8e3;
  }
  * { box-sizing: border-box; margin: 0; padding: 0; }
  html, body { width: 1200px; height: 879px; overflow: hidden; }
  body {
    background: var(--backdrop);
    font-family: "Questrial", "Century Gothic", sans-serif;
    color: var(--cocoa);
    position: relative;
  }
  .card {
    position: absolute;
    left: 280px;
    width: 640px;
    height: 366px;
    border-radius: 4px;
    overflow: hidden;
    box-shadow: 0 6px 18px rgba(0,0,0,0.12);
  }

  /* Front side */
  .card-front { top: 50px; background: var(--harbor-teal); }
  .front-pattern {
    position: absolute; inset: 0;
    background: radial-gradient(circle at 50% 45%, #6ccbcc 0%, var(--harbor-teal) 55%, var(--teal-deep) 100%);
  }
  .front-wordmark {
    position: absolute; inset: 0;
    display: flex; flex-direction: column; align-items: center; justify-content: center;
    color: var(--paper);
    font-size: 66px;
    line-height: 1.05;
    letter-spacing: 0.5px;
  }
  .front-wordmark .wordmark-sub { font-size: 40px; letter-spacing: 1px; }

  /* Back side */
  .card-back { top: 463px; background: var(--paper); }
  .back-logo {
    position: absolute; left: 0; top: 0; width: 270px; height: 230px;
    display: flex; flex-direction: column; align-items: center; justify-content: center;
    color: var(--harbor-teal);
    font-size: 38px; line-height: 1.05;
  }
  .back-logo .wordmark-sub { font-size: 24px; letter-spacing: 0.5px; }
  .divider {
    position: absolute; left: 280px; top: 44px; width: 1.5px; height: 232px;
    background: var(--cocoa);
  }
  .contact { position: absolute; left: 304px; top: 62px; right: 16px; }
  .contact-name { color: var(--harbor-teal); font-size: 30px; line-height: 1.1; }
  .contact-title { font-size: 16px; margin-top: 4px; }
  .contact-list { list-style: none; margin-top: 14px; }
  .contact-list li {
    display: flex; align-items: center; gap: 10px;
    font-size: 14.5px; line-height: 1.6;
  }
  .contact-list svg { width: 13px; height: 13px; flex: none; }
  .hours-band {
    position: absolute; left: 0; right: 0; bottom: 0; height: 90px;
    background: var(--harbor-teal);
  }
  .hours-first {
    position: absolute; left: 22px; top: 14px;
    font-size: 14px; color: var(--paper);
  }
  .hours-heading {
    position: absolute; left: 240px; top: 8px;
    font-size: 28px; color: var(--cocoa);
  }
  .hours-list {
    position: absolute; left: 240px; right: 16px; top: 54px;
    display: flex; gap: 48px;
    list-style: none; color: var(--paper); font-size: 14px;
  }
  .hours-list li::before { content: "•"; color: var(--cocoa); margin-right: 8px; }
</style>
</head>
<body>

  <section class="card card-front" aria-label="Card front">
    <div class="front-pattern" role="img" aria-label="Subtle tone-on-tone teal damask pattern"></div>
    <div class="front-wordmark">
      <span>Marbrook</span>
      <span class="wordmark-sub">Cupcakes</span>
    </div>
  </section>

  <section class="card card-back" aria-label="Card back">
    <div class="back-logo">
      <span>Marbrook</span>
      <span class="wordmark-sub">Cupcakes</span>
    </div>
    <div class="divider"></div>

    <div class="contact">
      <p class="contact-name">Renata Vasquill</p>
      <p class="contact-title">Assistant Operations Manager</p>
      <ul class="contact-list">
        <li>
          <svg viewBox="0 0 14 14" aria-hidden="true"><rect x="1" y="3" width="12" height="8" rx="1" fill="var(--harbor-teal)"/><path d="M1.5 3.5 L7 8 L12.5 3.5" stroke="#fff" stroke-width="1.2" fill="none"/></svg>
          renata@marbrookcupcakes.example
        </li>
        <li>
          <svg viewBox="0 0 14 14" aria-hidden="true"><path d="M3 1 L5.5 1 L6.5 4 L5 5.2 Q6.2 7.8 8.8 9 L10 7.5 L13 8.5 L13 11 Q13 13 11 13 Q2 12 1 3 Q1 1 3 1 Z" fill="var(--harbor-teal)"/></svg>
          T555.318.9047
        </li>
        <li>
          <svg viewBox="0 0 14 14" aria-hidden="true"><path d="M7 1 L13 6.5 L11.5 6.5 L11.5 13 L8.5 13 L8.5 9 L5.5 9 L5.5 13 L2.5 13 L2.5 6.5 L1 6.5 Z" fill="var(--harbor-teal)"/></svg>
          2735 Quarry Ln, Dallas TX 75999
        </li>
        <li>
          <svg viewBox="0 0 14 14" aria-hidden="true"><circle cx="7" cy="7" r="6" fill="var(--harbor-teal)"/><path d="M1 7 H13 M7 1 Q3.5 7 7 13 M7 1 Q10.5 7 7 13" stroke="#fff" stroke-width="0.9" fill="none"/></svg>
          www.marbrookcupcakes.example
        </li>
      </ul>
    </div>

    <div class="hours-band">
      <p class="hours-first">Mon-Thu: 10 AM - 9 PM</p>
      <p class="hours-heading">Store Hours:</p>
      <ul class="hours-list">
        <li>Fri-Sat: 10 AM - 10 PM</li>
        <li>Sun: 12 PM - 7 PM</li>
      </ul>
    </div>
  </section>

</body>
</html>
```